The hardcover "Velvet Register" (large size, Quarto 4º, 12 × 9 1/2 in, 30.5 × 24.15 cm) in German language as follows:

SAMTENES REGISTER (title)
der herausragendsten Unternehmer und Manager Deutschlands 2013 (subtitle 1)
BERLIN UND BRANDENBURG (subtitle 2, smaller than subtitle 1)

Korvalix (logo, WMF file attached)

Reason: The solutions are rather too childish and pre-made styles... is there anyone who can make it better? - a professional-looking business book (encyclopedia style, should have no color-pictures, no author's name, logo smaller due to the large size book)

Target Market(s)

business community

Requirements
Must have
• encyclopedia style large size book
must look professional and expensive

Nice to have
• - gold-color hardcover, or some gold-color elements
- some simple and decent graphic element (e.g. an ancient column, or some other architectural detail), if any
Should not have
• no color-pictures
no author's name

```html
<!DOCTYPE html>
<html lang="de">
<head>
<meta charset="utf-8">
<title>Samtenes Register – Hardcover</title>
<link href="https://fonts.googleapis.com/css2?family=Antonio:wght@400;600;700&display=swap" rel="stylesheet">
<style>
  :root {
    --page-bg: #ffffff;
    --cover-gold: #827249;
    --ink-white: #ffffff;
    --emblem-gold: #8a7a4e;
  }
  html, body {
    margin: 0;
    padding: 0;
    width: 1200px;
    height: 1000px;
    overflow: hidden;
    background: var(--page-bg);
  }
  .canvas {
    position: relative;
    width: 1200px;
    height: 1000px;
    background: var(--page-bg);
  }
  .cover {
    position: absolute;
    left: 204px;
    top: 0;
    width: 792px;
    height: 1000px;
    background: var(--cover-gold);
    font-family: "Antonio", "Arial Narrow", sans-serif;
    color: var(--ink-white);
    text-align: center;
    overflow: hidden;
  }
  .emblem-band {
    position: absolute;
    left: 336px;
    top: 0;
    width: 123px;
    height: 222px;
    background: var(--ink-white);
  }
  .emblem-art {
    position: absolute;
    left: 7px;
    top: 97px;
    width: 110px;
    height: 118px;
    background: var(--emblem-gold);
  }
  .title {
    position: absolute;
    left: 0;
    right: 0;
    top: 214px;
    margin: 0;
    font-weight: 700;
    font-size: 178px;
    line-height: 170px;
    letter-spacing: 0;
    text-transform: uppercase;
    transform: scaleX(0.84);
    transform-origin: center top;
  }
  .title-line {
    display: block;
  }
  .subtitle {
    position: absolute;
    left: 0;
    right: 0;
    top: 592px;
    margin: 0;
    font-weight: 400;
    font-size: 19.5px;
    line-height: 28px;
    letter-spacing: 0;
  }
  .region {
    position: absolute;
    left: 0;
    right: 0;
    top: 637px;
    margin: 0;
    font-weight: 600;
    font-size: 12.5px;
    line-height: 18px;
    letter-spacing: 0.7px;
    text-transform: uppercase;
  }
  .publisher {
    position: absolute;
    left: 0;
    right: 0;
    top: 914px;
    margin: 0;
    font-weight: 700;
    font-size: 30px;
    line-height: 38px;
    letter-spacing: 0.5px;
  }
</style>
</head>
<body>
<div class="canvas">
  <section class="cover">
    <div class="emblem-band">
      <div class="emblem-art" role="img" aria-label="Emblem: klassischer Tempelgiebel mit Säulen"></div>
    </div>
    <h1 class="title">
      <span class="title-line">Samtenes</span>
      <span class="title-line">Register</span>
    </h1>
    <p class="subtitle">der herausragendsten Unternehmer und Manager Deutschlands 2013</p>
    <p class="region">Berlin und Brandenburg</p>
    <p class="publisher">Korvalix</p>
  </section>
</div>
</body>
</html>
```